Infographics for nature conservation project / Infografiken für ein Naturschutzprojekt
Zielgruppe
Harrow Wildlife Trust (HWT) is an international conservation organisation based in Germany that has been implementing conservation projects in outstanding natural places in Africa, South America, South-East Asia, and Europe for decades. The HWT Continental Initiative safeguards large, biodiverse wilderness areas, mainly in Eastern Europe.
Since this year, a 5-year project (www.openmarshland.org), kicked-off to save the landscape of Belarusian and Ukrainian Polesia. Therefore, a consortium of nature conservation organisations from 4 different countries joined forces to protect this natural landscape:
• KRN-WingWatch Belarus
• DOTM-WingWatch Ukraine
• Caledon Society for Avian Study
• Harrow Wildlife Trust https://hwt-nature.org/en/projects/polesia-europes-largest-wilderness-area/
Polesia is one of the biggest and most impressive wilderness areas in Europe. It spans over 180,000 square kilometres and stretches across the boundaries of Poland, Belarus, Ukraine and Russia. With its naturally meandering river, gigantic mires, wetlands and floodplain forests, Polesia is a treasure for birds, amphibians and many other animal and plant species. It is not only key to wildlife, but also to human beings by providing reams of vital benefits as e.g. contributing to a country’s economy, regulating climate, providing clean water, storing carbon, supporting human health and many more.
Here (https://hwt-nature.org/en/news/amazonia-europe/) you will find a description and some pictures of the area and the website (www.openmarshland.org) on which the infographics will be presented..
The target group is the donor, but also media, local political decision makers, and the international conservation community will visit the website.
Aufgabenstellung
The designer should create six (6) infographics. The infographics will be used on the project website www.openmarshland.org to give a short and comprehensive introduction to the project.
The designer is free to choose, whether all infographics will be created as stand alone graphics or interconnected in one single file (examples below). This is up to the designers creativity and ideas, we are open for both suggestions.
If the designer choses the latter, having both a landscape- and a portrait- layout version for the different layouts of the website on a desktop and smartphone would be preferred (not mandatory).
The infographics will need to be incorporated into the website ideally by Friday,8th of May.
The six infographics needed should resemble, respectively, the:
1. General project facts: Project duration 2019-2023 (5 years), Partnership of 4 NGOs, Project area and size: 5.8 mio ha (located along Belarusian-Ukrainian border)
2. Project outcome 1: Biodiversity is better protected through the expansion by at least 100,000 ha, improved financing and international recognition of the protected area network in the core project area --> Expansion of protected areas by 100,000 hectare
3. Project outcome 2: Improved management and on-site protection in the protected and interconnected core area of over 1 Mio ha --> Improvement of protected areas management in over 1 million hectare
4. Project outcome 3: Mires and wetlands (6,000 ha) rewetted --> Restoration of 6,000 hectares of drained mires
5. Project outcome 4: Awareness and knowledge in relation to Polesia increased among the local population which leads to active support towards the conservation of key areas --> Increase of awareness and knowledge
6. Project outcome 5: Development of alternative livelihoods based on sustainable use of nature. In this way, nature-based jobs will be created which will replace other harmful practices in the area. --> Development of al..

```html
<!DOCTYPE html>
<html lang="en">
<head>
<meta charset="utf-8">
<title>General Project Facts</title>
<link href="https://fonts.googleapis.com/css2?family=Montserrat:wght@400;600;700;800&display=swap" rel="stylesheet">
<style>
  :root{
    --navy:#1a3f7c;
    --green:#8aac50;
    --bg:#f7f7f8;
    --white:#ffffff;
    --shadow:rgba(20,30,60,.18);
  }
  *{margin:0;padding:0;box-sizing:border-box}
  html,body{width:1200px;height:1068px;overflow:hidden;background:var(--bg)}
  body{position:relative;font-family:"Montserrat",Arial,sans-serif}
  .stage{position:absolute;inset:0}
  .title{position:absolute;right:35px;top:16px;text-align:right;line-height:1}
  .title .line1{font-size:29px;color:var(--navy);letter-spacing:.5px}
  .title .line1 b{font-weight:800}
  .title .line1 span{font-weight:400}
  .title .rule{height:3px;margin:8px 0 7px auto;width:272px;
    background:repeating-linear-gradient(90deg,#fff 0 8px,transparent 8px 13px)}
  .title .line2{font-size:29px;font-weight:800;color:var(--green)}
  .fact{position:absolute;top:100px;width:130px;text-align:center;color:var(--navy)}
  .fact .figure{font-size:19px;font-weight:700;color:var(--green);height:24px}
  .fact .figure small{font-size:13px}
  .fact .icon{display:block;margin:6px auto 4px}
  .fact .label{font-size:11.5px;font-weight:700;line-height:1.4}
  .box{position:absolute;width:314px;height:94px;display:flex;align-items:center;justify-content:center;
    text-align:center;color:var(--white);font-weight:700;font-size:14px;line-height:1.45;letter-spacing:.3px;
    padding:0 14px;box-shadow:4px 4px 6px var(--shadow)}
  .box::after{content:"";position:absolute;top:50%;transform:translateY(-50%);border:11px solid transparent}
  .box.left::after{right:-22px;border-left-color:inherit}
  .box.right::after{left:-22px;border-right-color:inherit}
  .box.navy{background:var(--navy);border-color:var(--navy)}
  .box.green{background:var(--green);border-color:var(--green)}
  .rings{position:absolute;left:0;top:0}
  .badge-num{font-family:"Montserrat",Arial,sans-serif;font-size:28px;font-weight:400;fill:#fff}
  .brand{position:absolute;left:928px;top:804px;width:240px;height:240px;border-radius:50%;
    background:var(--white);box-shadow:0 6px 18px var(--shadow);display:flex;
    align-items:center;justify-content:center;text-align:center}
  .brand .name{font-size:27px;font-weight:800;color:var(--navy);letter-spacing:1px;line-height:1.1;white-space:nowrap}
</style>
</head>
<body>
<div class="stage">

  <header class="title">
    <div class="line1"><b>GENERAL</b> <span>PROJECT</span></div>
    <div class="rule"></div>
    <div class="line2">FACTS</div>
  </header>

  <div class="fact" style="left:816px">
    <div class="figure">5 <small>years</small></div>
    <svg class="icon" width="76" height="76" role="img" aria-label="Clock with circular arrow showing project duration">
      <circle cx="38" cy="38" r="34" fill="var(--green)" opacity=".85"/>
      <circle cx="38" cy="38" r="24" fill="var(--navy)" opacity=".85"/>
    </svg>
    <div class="label">Project duration<br>2019-2023</div>
  </div>

  <div class="fact" style="left:928px">
    <div class="figure">4 NGOs</div>
    <svg class="icon" width="90" height="76" role="img" aria-label="Handshake symbolising the partnership">
      <rect x="4" y="18" width="82" height="44" rx="20" fill="var(--navy)" opacity=".85"/>
      <rect x="44" y="18" width="42" height="30" rx="14" fill="var(--green)"/>
    </svg>
    <div class="label">Partnership</div>
  </div>

  <div class="fact" style="left:1038px">
    <div class="figure">5.8 <small>mio ha</small></div>
    <svg class="icon" width="90" height="76" role="img" aria-label="Folded map with size arrows">
      <defs><linearGradient id="mapTone" x1="0" x2="1"><stop offset="0" stop-color="#7cc24a"/><stop offset="1" stop-color="#4a9bd0"/></linearGradient></defs>
      <rect x="6" y="10" width="62" height="46" fill="url(#mapTone)"/>
      <path d="M80 6v52M75 12l5-6 5 6M75 52l5 6 5-6" stroke="var(--green)" stroke-width="3" fill="none"/>
      <path d="M16 66h46M22 61l-6 5 6 5M56 61l6 5-6 5" stroke="var(--green)" stroke-width="3" fill="none"/>
    </svg>
    <div class="label">located along<br>Belarusian-Ukrainian<br>border</div>
  </div>

  <svg class="rings" width="1200" height="1068" viewBox="0 0 1200 1068">
    <defs>
      <filter id="soft" x="-30%" y="-30%" width="160%" height="160%">
        <feDropShadow dx="0" dy="4" stdDeviation="6" flood-color="#1a2a4a" flood-opacity=".18"/>
      </filter>
    </defs>

    <g class="step">
      <circle cx="491" cy="229" r="126" fill="none" stroke="var(--navy)" stroke-width="1"/>
      <circle cx="491" cy="229" r="116" fill="none" stroke="var(--navy)" stroke-width="8"/>
      <circle cx="491" cy="229" r="88" fill="var(--white)" filter="url(#soft)"/>
      <circle cx="491" cy="229" r="82" fill="none" stroke="var(--navy)" stroke-width="1"/>
      <rect role="img" aria-label="Protected area outline with location pin" x="434" y="178" width="116" height="110" rx="10" fill="var(--green)" opacity=".85"/>
      <circle cx="404" cy="314" r="41" fill="var(--navy)" filter="url(#soft)"/>
      <text class="badge-num" x="404" y="324" text-anchor="middle">1</text>
    </g>

    <g class="step">
      <circle cx="711" cy="380" r="126" fill="none" stroke="var(--green)" stroke-width="1"/>
      <circle cx="711" cy="380" r="116" fill="none" stroke="var(--green)" stroke-width="8"/>
      <circle cx="711" cy="380" r="88" fill="var(--white)" filter="url(#soft)"/>
      <circle cx="711" cy="380" r="82" fill="none" stroke="var(--green)" stroke-width="1"/>
      <rect role="img" aria-label="Map with binoculars" x="654" y="340" width="116" height="82" rx="6" fill="var(--navy)" opacity=".85"/>
      <circle cx="750" cy="267" r="41" fill="var(--green)" filter="url(#soft)"/>
      <text class="badge-num" x="750" y="277" text-anchor="middle">2</text>
    </g>

    <g class="step">
      <circle cx="491" cy="533" r="126" fill="none" stroke="var(--green)" stroke-width="1"/>
      <circle cx="491" cy="533" r="116" fill="none" stroke="var(--green)" stroke-width="8"/>
      <circle cx="491" cy="533" r="88" fill="var(--white)" filter="url(#soft)"/>
      <circle cx="491" cy="533" r="82" fill="none" stroke="var(--green)" stroke-width="1"/>
      <rect role="img" aria-label="Reeds and wetland grasses" x="434" y="478" width="116" height="110" rx="10" fill="var(--navy)" opacity=".85"/>
      <circle cx="612" cy="537" r="41" fill="var(--green)" filter="url(#soft)"/>
      <text class="badge-num" x="612" y="547" text-anchor="middle">3</text>
    </g>

    <g class="step">
      <circle cx="711" cy="686" r="126" fill="none" stroke="var(--green)" stroke-width="1"/>
      <circle cx="711" cy="686" r="116" fill="none" stroke="var(--green)" stroke-width="8"/>
      <circle cx="711" cy="686" r="88" fill="var(--white)" filter="url(#soft)"/>
      <circle cx="711" cy="686" r="82" fill="none" stroke="var(--green)" stroke-width="1"/>
      <rect role="img" aria-label="Speaker with megaphone addressing a group" x="652" y="648" width="118" height="76" rx="8" fill="var(--navy)" opacity=".85"/>
      <circle cx="750" cy="804" r="41" fill="var(--green)" filter="url(#soft)"/>
      <text class="badge-num" x="750" y="814" text-anchor="middle">4</text>
    </g>

    <g class="step">
      <circle cx="491" cy="838" r="126" fill="none" stroke="var(--navy)" stroke-width="1"/>
      <circle cx="491" cy="838" r="116" fill="none" stroke="var(--navy)" stroke-width="8"/>
      <circle cx="491" cy="838" r="88" fill="var(--white)" filter="url(#soft)"/>
      <circle cx="491" cy="838" r="82" fill="none" stroke="var(--navy)" stroke-width="1"/>
      <circle role="img" aria-label="Three linked circles for water, wellbeing and farming livelihoods" cx="491" cy="836" r="56" fill="var(--green)" opacity=".85"/>
      <circle cx="404" cy="761" r="41" fill="var(--navy)" filter="url(#soft)"/>
      <text class="badge-num" x="404" y="771" text-anchor="middle">5</text>
    </g>
  </svg>

  <div class="box navy left" style="left:25px;top:159px">EXPANSION OF PROTECTED AREAS<br>BY 100,000 HECTARE</div>
  <div class="box green right" style="left:852px;top:325px">IMPROVEMENT OF PROTECTED AREAS<br>MANAGEMENT IN OVER<br>1 MILLION HECTARE</div>
  <div class="box green left" style="left:25px;top:483px">RESTORATION OF 6,000 HECTARES<br>OF DRAINED MIRES</div>
  <div class="box green right" style="left:852px;top:623px">INCREASE OF AWARENESS AND<br>KNOWLEDGE</div>
  <div class="box navy left" style="left:25px;top:789px">DEVELOPMENT OF ALTERNATIVE<br>LIVELIHOODS</div>

  <div class="brand">
    <div class="name">FENREACH<br>OPEN LANDS</div>
  </div>

</div>
</body>
</html>
```